KTJ Business Card

Create a Simple but Elegant business card for a Luxury Off Road Vehicle and Accessories sales Company. Center of Letters we usually fill with red or a carbon fiber we don't want to limit creativity so anything goes. I think we would prefer large logo on the front and a smaller logo with infused QR reader on the back.
Some Ideas to get you heading more in the right direction are to put them on a thicker cardstock with red edges and we would need our logo letter (KTJ) filled in with red. Example is the Vescarelli card in our brief. For the side with our info on it we are looking for our logo to include an embedded QR reader also in our brief.
Information to include 2 bullet points: Luxury Off Road Vehicle Sales / Custom Off Road Bumpers
Address:418 Pellmont Road, Suite 519, The Woodlands, Texas
Phone# 555-314-9027,
Website: WWW.KTJ-TRAILGEAR.EXAMPLE
Facebook: facebook.com/KTJTrailGear
Instagram: instagram.com/ktj_trailgear
Target Market(s)
Exotic Vehicle and Outdoor enthusiasts.
Industry/Entity Type
Business
Look and feel
Each slider illustrates characteristics of the customer's brand and the style your logo design should communicate.

```html
<!DOCTYPE html>
<html lang="en">
<head>
<meta charset="utf-8">
<title>KTJ Business Card</title>
<link rel="stylesheet" href="https://fonts.googleapis.com/css2?family=Arimo:wght@400;700&family=Lilita+One&display=swap">
<style>
  :root {
    --card-top: #ffffff;
    --card-bottom: #dadada;
    --ink: #1c1c1c;
    --accent-red: #e3161e;
    --accent-outline: #2a0a0a;
    --rule: #bdbdbd;
    --qr-fill: #cfcfcf;
  }
  html, body {
    margin: 0;
    padding: 0;
    overflow: hidden;
    background: #ffffff;
  }
  .card {
    position: relative;
    width: 1200px;
    height: 857px;
    overflow: hidden;
    background: linear-gradient(to bottom, var(--card-top) 0%, #f1f1f1 45%, var(--card-bottom) 100%);
    font-family: "Arimo", Arial, sans-serif;
    color: var(--ink);
  }
  .brand {
    position: absolute;
    top: 78px;
    right: 70px;
    display: flex;
    align-items: center;
    gap: 16px;
  }
  .brand-name {
    font-family: "Arimo", Arial, sans-serif;
    font-weight: 700;
    font-size: 76px;
    line-height: 1;
    letter-spacing: 4px;
    color: var(--accent-red);
  }
  .brand-mark {
    width: 74px;
    height: 74px;
  }
  .headline {
    position: absolute;
    top: 270px;
    left: 0;
    width: 100%;
    margin: 0;
    text-align: center;
    font-family: "Lilita One", "Arial Black", sans-serif;
    font-weight: 400;
    font-size: 56px;
    line-height: 1;
    letter-spacing: 1px;
    color: var(--accent-red);
    -webkit-text-stroke: 3px var(--accent-outline);
    paint-order: stroke fill;
  }
  .divider {
    position: absolute;
    top: 373px;
    left: 41px;
    width: 1130px;
    height: 0;
    border-top: 1.5px solid var(--rule);
  }
  .services {
    position: absolute;
    top: 400px;
    left: 0;
    width: 100%;
    margin: 0;
    padding: 0;
    list-style: none;
    display: flex;
    justify-content: center;
    gap: 70px;
    font-weight: 700;
    font-size: 28px;
    line-height: 1;
  }
  .services li::before {
    content: "";
    display: inline-block;
    width: 12px;
    height: 12px;
    margin-right: 14px;
    vertical-align: middle;
    border-radius: 50%;
    background: var(--accent-red);
  }
  .contact {
    position: absolute;
    left: 73px;
    top: 478px;
    margin: 0;
    padding: 0;
    list-style: none;
    font-size: 28px;
    line-height: 1;
  }
  .contact li { margin-bottom: 22px; }
  .qr-code {
    position: absolute;
    right: 82px;
    top: 482px;
    width: 170px;
    height: 170px;
    background: var(--qr-fill);
    border: 3px solid var(--ink);
    box-sizing: border-box;
  }
  .phone {
    position: absolute;
    right: 82px;
    top: 757px;
    margin: 0;
    font-weight: 700;
    font-size: 36px;
    line-height: 1;
  }
</style>
</head>
<body>
  <main class="card">
    <div class="brand">
      <span class="brand-name">KTJ</span>
      <svg class="brand-mark" viewBox="0 0 74 74" aria-hidden="true">
        <circle cx="37" cy="37" r="32" fill="none" stroke="#1c1c1c" stroke-width="6"/>
      </svg>
    </div>

    <h1 class="headline">Luxury Vehicle Sales and Accessories</h1>

    <div class="divider"></div>

    <ul class="services">
      <li>Luxury Off Road Vehicle Sales</li>
      <li>Custom Off Road Bumpers</li>
    </ul>

    <ul class="contact">
      <li class="website">WWW.KTJ-TRAILGEAR.EXAMPLE</li>
      <li class="email">info@ktj-trailgear.example</li>
      <li class="address">418 Pellmont Road, Suite 519, The Woodlands, Texas</li>
      <li class="facebook">facebook.com/KTJTrailGear</li>
      <li class="instagram">instagram.com/ktj_trailgear</li>
    </ul>

    <div class="qr-code" role="img" aria-label="QR code linking to the KTJ website"></div>

    <p class="phone">Phone # 555.314-9027</p>
  </main>
</body>
</html>
```